Young adult personal development needs podcast 1400x1400 logo

We need artwork done for a podcast logo. The podcast is called The Brightwillers Podcast and is aimed at ages 20-30 waking up and wanting to make changes in their lives.

Using either of the two photos with the logo at bottom right of picture.

Somewhere it says: The Brightwillers Podcast: Educating & inspiring you to reach your greatest potential.

"The Brightwillers Podcast: Educating & inspiring you to reach your greatest potential.

With a strong belief in mentors and role models being a key factor to anyones success, Marcus has placed himself along side the best in their fields.

Diving into movement, primal patterns, mindfulness, creativity and even the influence our gut has over our brain, these experts are going to show you how these pieces paint the picture that is your greatest potential."

Industry/Entity Type

Adult

```html
<!DOCTYPE html>
<html lang="en">
<head>
<meta charset="UTF-8">
<title>The Brightwillers Podcast</title>
<link rel="stylesheet" href="https://fonts.googleapis.com/css2?family=Libre+Baskerville:wght@400;700&family=Arimo:wght@400&display=swap">
<style>
  :root {
    --teal: #7aafb1;
    --white: #ffffff;
    --page: #ffffff;
    --url-grey: #8a8a8a;
    --sky-top: #e9e4e2;
    --sky-low: #dedbd9;
    --sea: #a9b3b7;
    --shore: #7d8a6a;
    --scrub: #4f5a3c;
  }
  html, body {
    margin: 0;
    padding: 0;
    width: 1200px;
    height: 1200px;
    overflow: hidden;
    background: var(--page);
  }
  .cover {
    position: relative;
    width: 1200px;
    height: 1200px;
    background: var(--page);
    font-family: "Libre Baskerville", Georgia, serif;
  }
  .title-band {
    position: absolute;
    left: 16px;
    top: 13px;
    width: 1168px;
    height: 387px;
    background: var(--teal);
    display: flex;
    align-items: center;
    justify-content: center;
  }
  .show-title {
    margin: 0;
    color: var(--white);
    font-weight: 700;
    font-size: 104px;
    line-height: 1.12;
    text-align: center;
    letter-spacing: 0.5px;
  }
  .hero-photo {
    position: absolute;
    left: 16px;
    top: 413px;
    width: 1168px;
    height: 603px;
    background: linear-gradient(to bottom,
      var(--sky-top) 0%,
      var(--sky-low) 55%,
      var(--sea) 57%,
      var(--sea) 70%,
      var(--shore) 74%,
      var(--scrub) 100%);
  }
  .brand-mark {
    position: absolute;
    right: 40px;
    bottom: 34px;
    color: var(--white);
    font-family: "Libre Baskerville", Georgia, serif;
    font-weight: 400;
    font-size: 26px;
    letter-spacing: 4px;
    text-transform: uppercase;
  }
  .tagline-band {
    position: absolute;
    left: 16px;
    top: 1027px;
    width: 1168px;
    height: 117px;
    background: var(--teal);
    display: flex;
    align-items: center;
    justify-content: center;
  }
  .tagline {
    margin: 0;
    color: var(--white);
    font-weight: 400;
    font-size: 34px;
    text-align: center;
  }
  .site-url {
    position: absolute;
    left: 0;
    right: 0;
    top: 1164px;
    text-align: center;
    color: var(--url-grey);
    font-family: "Arimo", Arial, sans-serif;
    font-size: 19px;
    letter-spacing: 0.5px;
  }
</style>
</head>
<body>
  <main class="cover">
    <header class="title-band">
      <h1 class="show-title">The Brightwillers<br>Podcast</h1>
    </header>

    <section class="hero-photo" role="img" aria-label="Photo of a long-haired man seen from behind with arms spread wide, overlooking coastal scrubland and a calm grey sea under an overcast sky">
      <div class="brand-mark">Arlo Growth</div>
    </section>

    <footer class="tagline-band">
      <p class="tagline">Educating, Inspiring you to reach your Greatest Potential.</p>
    </footer>

    <div class="site-url">WWW.YOURBRAND.COM</div>
  </main>
</body>
</html>
```